Business Card Design for Event Planning Company

Create a business card for event planning company using our new logo. After I pick the design, I will need files made for 6 employees. Our company provides event design & logistics services as well as venue management. The font should be sans serif and complementary to the logo. I will need to know the name of the font selected for the final design. The phone numbers listed should be separated by "." not "-"

Address for the card
PO Box 218, Washington, DC 20019

Card One
Lorna Pettigrew
lpettigrew@galaplanora.com
202.481.7032

Card Two
Marisol Dunleavy
mdunleavy@galaplanora.com
202.416.2950

Card Three
Rebecca Vasquetti
rvasquetti@galaplanora.com
978.527.6043

Card Four
Tessa Brink
tbrink@galaplanora.com
202.458.1276

Card Five
Ada-Rose Pemberton-Nwaku
adarose@galaplanora.com
202.819.3047

Card Six
Valerie Thornbury
Valerie@galaplanora.com
202.592.8134

Target Market(s)

Corporate/Non-Profit

Industry/Entity Type

Event Planning

Contact Information for Business Card

Address for the card

Card One
Lorna Pettigrew
lpettigrew@galaplanora.com
202.481.7032

Card Two
Marisol Dunleavy
202.416.2950

Card Three
Rebecca Vasquetti
978.527.6043

Card Four
Tessa Brink
tbrink@galaplanora.com
202.458.1276

Card Five
Ada-Rose Pemberton-Nwaku
202.819.3047

Card Six
Valerie Thornbury
202.592.8134

Font styles to use
Sans Serif

Colors

Designer to choose colors to be used in the design.

Requirements
Must have
• Two-sided with logo
Should not have
• Extra colors or be too busy

```html
<!DOCTYPE html>
<html lang="en">
<head>
<meta charset="utf-8">
<title>Gala Planora – Business Card</title>
<link href="https://fonts.googleapis.com/css2?family=Montserrat:wght@700&family=Questrial&display=swap" rel="stylesheet">
<style>
  :root {
    --teal: #5ea5a2;
    --ink: #0e0e0e;
    --paper: #ffffff;
    --stage: #dcdcdc;
    --wordmark: #222222;
  }
  html, body {
    margin: 0;
    padding: 0;
    width: 1200px;
    height: 910px;
    overflow: hidden;
    background: var(--stage);
  }
  .sheet {
    position: relative;
    width: 1200px;
    height: 910px;
  }
  .card {
    position: absolute;
    left: 250px;
    width: 700px;
    height: 400px;
    background: var(--paper);
    box-shadow: 0 6px 18px rgba(0,0,0,0.18);
    overflow: hidden;
  }
  .card--front { top: 35px; }
  .card--back  { top: 475px; }
  .card__shapes {
    position: absolute;
    inset: 0;
    width: 100%;
    height: 100%;
  }
  .shape--teal { fill: var(--teal); }
  .shape--ink  { fill: var(--ink); }

  .wordmark {
    position: absolute;
    display: flex;
    align-items: center;
    gap: 14px;
    font-family: "Questrial", sans-serif;
    color: var(--wordmark);
    letter-spacing: 1px;
    white-space: nowrap;
  }
  .wordmark__dot {
    border-radius: 50%;
    background: var(--teal);
    flex: none;
  }
  .card--front .wordmark {
    left: 70px;
    top: 165px;
    font-size: 58px;
  }
  .card--front .wordmark__dot { width: 34px; height: 34px; }
  .card--back .wordmark {
    left: 400px;
    top: 95px;
    font-size: 34px;
  }
  .card--back .wordmark__dot { width: 20px; height: 20px; }

  .holder {
    position: absolute;
    left: 60px;
    top: 95px;
    margin: 0;
    font-family: "Montserrat", sans-serif;
    font-weight: 700;
    font-size: 30px;
    color: var(--paper);
    letter-spacing: -0.3px;
  }
  .contact {
    position: absolute;
    left: 40px;
    top: 268px;
    margin: 0;
    padding: 0;
    list-style: none;
    font-family: "Questrial", sans-serif;
    font-size: 16px;
    color: var(--paper);
  }
  .contact__item {
    display: flex;
    align-items: center;
    gap: 9px;
    height: 33px;
  }
  .contact__icon {
    width: 17px;
    height: 17px;
    flex: none;
  }
</style>
</head>
<body>
<main class="sheet">

  <section class="card card--front" aria-label="Card front">
    <svg class="card__shapes" viewBox="0 0 700 400" preserveAspectRatio="none" aria-hidden="true">
      <polygon class="shape--teal" points="700,0 700,400 476,400"/>
      <polygon class="shape--ink" points="651,0 700,0 476,400 0,400 0,376 434,376"/>
    </svg>
    <div class="wordmark">
      <span>galaplanora</span>
      <span class="wordmark__dot"></span>
    </div>
  </section>

  <section class="card card--back" aria-label="Card back">
    <svg class="card__shapes" viewBox="0 0 700 400" preserveAspectRatio="none" aria-hidden="true">
      <polygon class="shape--teal" points="0,24 252,24 476,400 0,400"/>
      <polygon class="shape--ink" points="0,0 287,0 525,400 476,400 252,24 0,24"/>
    </svg>
    <div class="wordmark">
      <span>galaplanora</span>
      <span class="wordmark__dot"></span>
    </div>

    <h1 class="holder">Lorna Pettigrew</h1>

    <ul class="contact">
      <li class="contact__item">
        <svg class="contact__icon" viewBox="0 0 17 17" aria-hidden="true">
          <rect width="17" height="17" rx="2" fill="#fff"/>
          <path d="M5 3.5 L7 6.5 L6 7.8 C6.8 9.4 7.8 10.4 9.3 11.1 L10.5 10 L13.5 12 L12.6 13.6 C8 13.4 3.6 9 3.4 4.4 Z" fill="var(--teal)"/>
        </svg>
        <span>202.481.7032</span>
      </li>
      <li class="contact__item">
        <svg class="contact__icon" viewBox="0 0 17 17" aria-hidden="true">
          <rect width="17" height="17" rx="2" fill="#fff"/>
          <text x="8.5" y="12.6" text-anchor="middle" font-family="Questrial, sans-serif" font-size="12" fill="var(--teal)">@</text>
        </svg>
        <span>lpettigrew@galaplanora.com</span>
      </li>
      <li class="contact__item">
        <svg class="contact__icon" viewBox="0 0 17 17" aria-hidden="true">
          <rect width="17" height="17" rx="2" fill="#fff"/>
          <rect x="3" y="5" width="11" height="7.5" fill="none" stroke="var(--teal)" stroke-width="1.2"/>
          <path d="M3 5 L8.5 9.5 L14 5" fill="none" stroke="var(--teal)" stroke-width="1.2"/>
        </svg>
        <span>PO Box 218, Washington, DC 20019</span>
      </li>
    </ul>
  </section>

</main>
</body>
</html>
```